Progressive Architecture and Urban Planning Studio - Stationery Design

The Kestrel Collective: a small boutique Architectural and Urban Planning Studio based in Natal/ RN, Brazil, about to open branches in South Africa and West Africa, established to provide high quality, innovative design and personal client service for projects worldwide. Our approach to Architecture: Minimal - Less is More, so to speak, but with an edge! Strive to produce "clean" projects - stripped of all that can be stripped, no excesses. Got our Logo right here with Pixel Harbor, and hope to do the same with our stationery (were informed that includes business cards, letterhead and envelopes). Since we'll be using two clour schemes, we want at least one using a black background (business card). We'll also allow manipulation of our logo if it helps the final design. Good Luck!

Font styles to use
Other font styles liked:
• Nexa

Colors

Designer to choose colors to be used in the design.

Requirements
Must have
• Business Cards/ Letterheads with the following address:
Rua Olavo Pereira 2741, Vale Dourado, Serra Clara/PB
Should be able to edit it.

```html
<!DOCTYPE html>
<html lang="en">
<head>
<meta charset="utf-8">
<title>The Kestrel Collective — Letterhead</title>
<link rel="stylesheet" href="https://fonts.googleapis.com/css2?family=Arimo:wght@400;700&family=Pinyon+Script&display=swap">
<style>
  :root {
    --paper: #ffffff;
    --ink: #2b2b2b;
    --ink-soft: #3a3a3a;
    --accent: #e0242b;
    --muted: #555555;
  }
  * { margin: 0; padding: 0; box-sizing: border-box; }
  html, body { width: 928px; height: 1200px; overflow: hidden; background: var(--paper); }
  .letterhead {
    position: relative;
    width: 928px;
    height: 1200px;
    background: var(--paper);
    font-family: "Arimo", Arial, sans-serif;
    color: var(--ink);
  }
  .brand {
    position: absolute;
    left: 34px;
    top: 52px;
    display: flex;
    align-items: center;
    gap: 20px;
  }
  .brand-square {
    width: 30px;
    height: 30px;
    background: var(--accent);
  }
  .brand-name {
    font-size: 19px;
    font-weight: 400;
    letter-spacing: 4px;
    color: var(--ink);
    text-transform: uppercase;
  }
  .contact {
    position: absolute;
    left: 678px;
    top: 38px;
    font-size: 9.5px;
    line-height: 12px;
    font-style: normal;
    color: var(--muted);
  }
  .contact .address { margin-bottom: 4px; }
  .contact .row { color: var(--ink); }
  .contact .row-gap { margin-top: 2px; }
  .contact .label { color: var(--accent); font-weight: 700; }
  .salutation {
    position: absolute;
    left: 62px;
    top: 205px;
    font-size: 16.5px;
    color: var(--ink-soft);
  }
  .body-text {
    position: absolute;
    left: 133px;
    top: 240px;
    width: 740px;
    font-size: 16.3px;
    line-height: 20.7px;
    color: var(--ink-soft);
  }
  .body-text p { margin-bottom: 20.7px; white-space: nowrap; }
  .signature {
    position: absolute;
    left: 56px;
    top: 882px;
    font-family: "Pinyon Script", cursive;
    font-size: 50px;
    color: var(--ink);
  }
  .footer-web {
    position: absolute;
    right: 22px;
    top: 1154px;
    font-size: 14px;
    color: var(--ink);
  }
</style>
</head>
<body>
<main class="letterhead">
  <header>
    <div class="brand">
      <span class="brand-square"></span>
      <span class="brand-name">The Kestrel Collective</span>
    </div>
    <address class="contact">
      <div class="address">Rua Olavo Pereira 2741, Vale Dourado, Serra Clara/PB</div>
      <div class="row"><span class="label">Tel :</span> +000 000 0000</div>
      <div class="row"><span class="label">Mob :</span> +000 000 0000</div>
      <div class="row row-gap"><span class="label">E-mail :</span> name@kestrelcollective.com</div>
      <div class="row"><span class="label">Web :</span> www.kestrelcollective.com</div>
    </address>
  </header>

  <p class="salutation">Dear Sir / Madam,</p>

  <section class="body-text">
    <p>Lorem ipsum dolor sit amet, consectetur adipisicing elit, sed do eiusmod tempor labore et<br>olore magna aliqua. Ut enim ad minim veniam, quis nostrud exercitation ullamco laboris nisi<br>ut aliquip ex ea commodo consequa.Lorem ipsum dolor sit amet, nsectetur adipisicing elit,<br>sed do eiusmod tempor incididunt ut labore et dolore magna aliqua. Ut enim ad minim<br>veniam, quis.</p>
    <p>Lorem ipsum dolor sit amet, consectetur adipisicing elit, sed do eiusmod tempor labore et<br>dolore magna aliqua. Ut enim ad minim veniam, quis nostrud exercitation ullamco laboris nisi<br>ut aliquip ex ea commodo consequa.Lorem ipsum dolor sit amet, nsectetur adipisicing elit,<br>sed do eiusmod tempor incididunt ut labore et dolore magna aliqua. Ut enim ad minim<br>veniam, quis.</p>
    <p>Lorem ipsum dolor sit amet, consectetur adipisicing elit, sed do eiusmod tempor labore et<br>dolore magna aliqua. Ut enim ad minim veniam, quis nostrud exercitation ullamco laboris nisi<br>ut aliquip ex ea commodo consequa.Lorem ipsum dolor sit amet, nsectetur adipisicing elit,<br>sed do eiusmod tempor incididunt ut labore et dolore magna aliqua. Ut enim ad minim<br>veniam, quis.</p>
    <p>Lorem ipsum dolor sit amet, consectetur adipisicing elit, sed do eiusmod tempor labore et<br>dolore magna aliqua. Ut enim ad minim veniam, quis nostrud exercitation ullamco laboris nisi<br>ut aliquip ex ea commodo consequa.Lorem ipsum dolor sit amet, nsectetur adipisicing elit,<br>sed do eiusmod tempor incididunt ut labore et dolore magna aliqua. Ut enim ad minim<br>veniam, quis.</p>
    <p>Lorem ipsum dolor sit amet, consectetur adipisicing elit, sed do eiusmod tempor labore et<br>dolore magna aliqua. Ut enim ad minim veniam, quis nostrud exercitation ullamco laboris nisi<br>ut aliquip ex ea commodo consequa.Lorem ipsum dolor sit amet, nsectetur adipisicing elit,<br>sed do eiusmod tempor incididunt ut labore et dolore magna aliqua. Ut enim ad minim<br>veniam, quis.</p>
  </section>

  <p class="signature">Your Name</p>

  <footer class="footer-web">www.kestrelcollective.com</footer>
</main>
</body>
</html>
```